Plakat-Design für Haushaltsreinigungen
Zielgruppe
Wir bieten haushaltsnahe Dienstleistungen für Privathaushalte an. Wir sind spezialisiert auf Haushaltsreinigungen für pflegebedürftige Personen.
Aufgabenstellung
Es geht darum dass auf dem Plakat zu erkennen ist, dass wir Haushaltsreinigungen anbieten die mit der Pflegekasse mit dem monatlichen Entlastungsbetrag von 125,- € abgerechnet werden können. Viele pflegebdürftige Personen ab einem Pflegegrad 1 wissen nicht, dass speziell für die Entlastungs im Alltag (Haushaltshilfen) ein monatliches Budget bei der Pflegekasse liegt und über zertifzierte Dienstleister wie wir es sind, abgerufen werden können. Somit lassen die pflegebdürftigen Personen dass Geld bei der Kasse verfallen.
Nun möcten wir mit der Plakatwerbung zum einen für unser Dienstleistungsunternehmen Werbung machen und Neukunden gewinnen, und zum anderen soll es auf den monatlichen Entlastungsbetrag hinweisen.
Folgende Slogans, haben wir mal auf die Schnelle uns ausgedacht, welche eventuell auf dem Plakat stehen könnten.
- Haushaltshilfe für Pflegebedürftige
- Lindmoor Haushaltshilfen Abrechnung direkt über alle Pflegekassen
- Keine Zuzahlung ab Pflegegrad 1
- Nutzen Sie Ihren Entlastungsbetrag
- Haushaltshilfe ohne versteckte Kosten da direkt über Pflegekasse
- 125 € für Haushaltshilfe ab Pflegegrad 1
- Neu in Esslingen
Auf dem Plakat soll neben der allgemeinen Botschaft natürlich auch unser Logo und unsere Kontaktdaten abgebildet sein.
Die Kontaktdaten lauten:
www.lindmoor.de
E-Mail: info@lindmoor.de
Tel.: 0711 83 27 60 95
Unten aufgeführt noch die technischen Daten für das Plakat:
Die Größe das Plakats beträgt 9 m²
Dateiformat: 590mm x 410mm (Maßstab 1:6)
kein Beschnitt, keine Beschnittzeichen
Sicherheitsabstand 2 cm zum Rand
Datenformat: PDF/X4
Auflösung: mind. 150dpi, CMYK

```html
<!DOCTYPE html>
<html lang="de">
<head>
<meta charset="utf-8">
<title>Lindmoor Haushaltshilfen – Plakat</title>
<link rel="stylesheet" href="https://fonts.googleapis.com/css2?family=Cinzel:wght@600;700&family=Lato:wght@400;700;900&display=swap">
<style>
  :root {
    --brand-red: #d4102a;
    --band-red: #c81b30;
    --shadow-red: #8e1020;
    --ink: #2b2b2b;
    --paper: #ffffff;
    --stage: #e9e9eb;
  }
  html, body {
    margin: 0;
    width: 1200px;
    height: 1003px;
    overflow: hidden;
    background: var(--stage);
  }
  .poster {
    position: absolute;
    left: 20px;
    top: 85px;
    width: 1160px;
    height: 832px;
    background: var(--paper);
    box-shadow: 0 6px 24px rgba(0,0,0,.18);
  }
  .poster svg { display: block; }
  .serif { font-family: "Cinzel", "Times New Roman", serif; font-weight: 700; }
  .sans { font-family: "Lato", Arial, sans-serif; }
  .brand-name { fill: var(--ink); }
  .brand-tagline { fill: var(--brand-red); }
  .headline { fill: var(--brand-red); }
  .ribbon-text { fill: var(--paper); font-weight: 700; }
  .band-text { fill: var(--paper); }
  .price { fill: var(--brand-red); font-weight: 900; }
</style>
</head>
<body>
  <main class="poster">
    <svg width="1160" height="832" viewBox="0 0 1160 832" xmlns="http://www.w3.org/2000/svg">
      <defs>
        <linearGradient id="illustration-tone" x1="0" y1="0" x2="1" y2="1">
          <stop offset="0" stop-color="#ffffff"/>
          <stop offset="0.45" stop-color="#f6d27a"/>
          <stop offset="1" stop-color="#c81b30"/>
        </linearGradient>
        <linearGradient id="ribbon-shade" x1="0" y1="0" x2="0" y2="1">
          <stop offset="0" stop-color="#000" stop-opacity=".18"/>
          <stop offset="1" stop-color="#000" stop-opacity="0"/>
        </linearGradient>
      </defs>

      <!-- Illustration area -->
      <rect class="illustration" x="665" y="16" width="495" height="486" fill="url(#illustration-tone)" role="img" aria-label="Illustration: Haushaltshilfe beim Staubsaugen vor rotem Hintergrund"/>

      <!-- Brand -->
      <g class="brand">
        <circle cx="106" cy="100" r="34" fill="var(--brand-red)"/>
        <text class="serif brand-name" x="208" y="118" font-size="66" textLength="420" lengthAdjust="spacingAndGlyphs">LINDMOOR</text>
        <text class="serif brand-tagline" x="208" y="150" font-size="25" textLength="420" lengthAdjust="spacingAndGlyphs">HAUSHALTSHILFEN &amp; MEHR</text>
      </g>

      <!-- Message ribbon -->
      <g class="ribbon">
        <polygon points="48,473 623,477 640,512 78,520" fill="url(#ribbon-shade)"/>
        <polygon points="20,269 499,273 623,477 68,473" fill="var(--brand-red)"/>
        <text class="sans ribbon-text" x="95" y="348" font-size="47">Nutzen Sie Ihren</text>
        <text class="sans ribbon-text" x="95" y="414" font-size="47" textLength="453" lengthAdjust="spacingAndGlyphs">Entlastungsbetrag!</text>
      </g>

      <!-- Headline -->
      <text class="serif headline" x="37" y="621" font-size="74" textLength="1096" lengthAdjust="spacingAndGlyphs">HAUSHALTSHILFEN &amp; MEHR</text>

      <!-- Offer band -->
      <g class="offer-band">
        <rect x="200" y="651" width="960" height="181" fill="var(--band-red)"/>
        <path d="M0,651 H220 Q292,651 292,740 Q292,790 282,812 L305,822 Q240,832 200,832 H0 Z" fill="var(--shadow-red)"/>
        <path d="M0,651 H205 Q275,651 275,740 Q275,790 268,808 L290,818 Q230,832 190,832 H0 Z" fill="var(--paper)"/>
        <text class="sans price" x="132" y="756" font-size="80" text-anchor="middle" transform="rotate(-9 132 726)">125 €</text>

        <text class="sans band-text" x="323" y="717" font-size="70" textLength="446" lengthAdjust="spacingAndGlyphs"><tspan font-weight="400">ab </tspan><tspan font-weight="700">Pflegegrad 1</tspan></text>
        <text class="sans band-text" x="323" y="773" font-size="45" textLength="559" lengthAdjust="spacingAndGlyphs">125 € für Ihre Haushaltshilfe</text>
        <text class="sans band-text" x="325" y="817" font-size="33" textLength="800" lengthAdjust="spacingAndGlyphs">www.lindmoor.de, info@lindmoor.de,  0711 83 27 60 95</text>
      </g>
    </svg>
  </main>
</body>
</html>
```